We need a label for our new 8 oz. bottle and one for our 1 oz. sample. Bottle sizes are approximately 5 1/4 inch width X 6 1/4 height for 8 oz. and 3 1/2 inch width x 1 1/2 inch for 1 oz. Following is the narrative that we would like to see on the 8 oz. bottle;

Leaf Sentry is a versatile ecologically friendly plant supplement that stimulates the natural innate defense responses within plants to resist insects, pathogens, and soil-borne diseases.
Leaf Sentry increases photosynthesis, promotes and enhances plant growth, stimulates nutrient uptake, increases germination and sprouting, and boosts plant vigor.
Our commitment to you is reflected in our full time research center where our scientists are continually researching better ways to improve crop yields along with extensive research on the pre and post-harvest treatment of plants utilizing alternatives to synthetic fungicides, pesticides and fertilizers not only for you but also for the commercial farmer. Leaf Sentry has been specially developed for anyone who loves growing plants.

Active Ingredient
D-glucosamine- N-acetyl-glucosamine 1.00%
Other Ingredients ……...................... 99.00%
TOTAL…………………………………….100.00%
This product is exempt from regulation under 25(b) of FIFRA.
Manufactured by Verdalis Agrilabs Inc.
Saguaro Bend, AZ. 85399
Questions or Comments call (555) 318-4720

Recommended Use
Leaf Sentry may be applied several ways depending on where your plant is on its life cycle.

Important Note: This product does not replace regular fertilization applications.
Seeds: (1) Soak seeds in concentrate for 3 hours remove seeds (save & reuse concentrate) rinse, dry and plant. (2) Plant seeds in dirt add 1 teaspoon of concentrate to 16 oz. water and apply to planted seeds.
Transplant: (1) Add 2 tablespoons to a gallon of water. Pour water into a tray or large container and submerge seedling so that roots are in solution. Leave at least 3 hours and up to 24 hours. (2) After transplanting add ½ teaspoon to the base of plant and water.
Mature Plant: Add 1 tablespoon to 1 gallon of water and use and use mixture when preparing your favorite fertilizer.

KEEP OUT OF REACH OF CHILDREN

WARRANTY
Verdalis Agrilabs Inc. warrants that this product conforms to the chemical description on the label and is a reasonable fit for the purposes set forth in the Directions on this label when used in accordance with those Directions under the conditions described therein. TO THE EXTENT CONSISTENT WITH APPLICABLE LAW NO OTHER EXPRESS WARRANTY OR IMPLIED WARRANTY OF FITNESS FOR PARTICULAR PURPOSE OR MECHANTABILITY IS MADE. This warranty is also subject to the conditions and limitations stated herein.

Company Name should be at the top but should be small compared to the product name. Company Name "Verdalis Agrilabs Inc."

Product name; Leaf Sentry
Biocompatible-Biodegradable-Nontoxic
Safe for Organic Production
Verdalis Agrilabs Inc. prides itself on developing products that DO NOT harm humans, animals or the planet along with our commitment to sustainability.

Sample bottles should just have directions and name maybe some selling points.

Bottles are green and we believe the designer should have free range on how to design labels.

Target Market(s)

Gardeners in general 35 to 75. Although, there is interest in the marijuana growing community. But we feel that some of the designs used in that sector might be a bit loud. But, we also want something that will attract attention on the self.

Industry/Entity Type

Agriculture

Font styles to use
Decorative

Colors

Designer to choose colors to be used in the design.

Requirements
Must have
• Recommended use, Active ingredients and Warranty
Nice to have
• Existing print provided
Should not have
• Dead plants

```html
<!DOCTYPE html>
<html lang="en">
<head>
<meta charset="utf-8">
<title>Leaf Sentry – 8 oz Label</title>
<link rel="stylesheet" href="https://fonts.googleapis.com/css2?family=PT+Sans+Narrow:wght@400;700&display=swap">
<style>
  :root {
    --page: #ffffff;
    --frame: #6e665e;
    --deep-green: #3d7a3e;
    --mid-green: #6aa84a;
    --lime: #a9d35a;
    --lime-light: #c8e58a;
    --panel: rgba(230, 240, 205, 0.88);
    --panel-edge: #7fb25a;
    --ink: #1e2414;
    --badge: #2a1a12;
    --badge-text: #f2f2e6;
    --arch: #3f7e3c;
    --arch-text: #d8ebc0;
  }
  * { box-sizing: border-box; margin: 0; padding: 0; }
  html, body { width: 1200px; height: 1200px; overflow: hidden; background: var(--page); }
  body { position: relative; font-family: "PT Sans Narrow", "Arial Narrow", sans-serif; color: var(--ink); }

  .brand-name {
    position: absolute; left: 0; width: 1200px; top: 444px;
    text-align: center;
    font-family: "PT Sans Narrow", "Arial Narrow", sans-serif; font-weight: 400;
    font-size: 44px; line-height: 50px; color: var(--ink); letter-spacing: 1px;
  }

  .label {
    position: absolute; left: 56px; top: 526px; width: 1104px; height: 394px;
    border-radius: 16px; background: var(--frame); padding: 9px;
  }
  .label-face {
    position: relative; width: 100%; height: 100%; border-radius: 10px; overflow: hidden;
    background:
      radial-gradient(ellipse 55% 70% at 50% 40%, var(--lime-light) 0%, transparent 70%),
      linear-gradient(180deg, var(--deep-green) 0%, var(--lime) 9%, var(--lime) 78%, var(--mid-green) 88%, var(--deep-green) 100%);
  }
  .label-texture {
    position: absolute; inset: 0;
    background: linear-gradient(115deg, transparent 40%, rgba(255,255,255,0.12) 55%, transparent 70%);
  }

  .panel {
    position: absolute; background: var(--panel);
    border: 2px solid var(--panel-edge); border-radius: 6px;
  }
  .panel-directions { left: 23px; top: 19px; width: 310px; height: 340px; padding: 6px 5px; font-size: 11px; line-height: 15.6px; }
  .panel-info { left: 755px; top: 17px; width: 313px; height: 348px; padding: 5px 4px; font-size: 8.6px; line-height: 13px; }
  .panel p { margin: 0; }
  .lead { font-weight: 700; font-style: italic; }
  .spacer { height: 15.6px; }
  .panel-info .spacer { height: 14px; }
  .section-title { font-weight: 700; font-style: italic; font-size: 10.5px; line-height: 16px; }
  .ingredients { font-size: 10px; line-height: 16px; border-collapse: collapse; }
  .ingredients td { padding: 0; }
  .ingredients td.pct { padding-left: 3px; }
  .legal { text-align: center; font-size: 8.2px; line-height: 13px; }
  .body-sm { font-size: 10px; line-height: 16px; }

  .center {
    position: absolute; left: 333px; width: 422px; top: 0; text-align: center;
  }
  .company { margin-top: 15px; font-size: 12px; color: #2c3520; }
  .size-badge {
    position: absolute; left: 322px; top: 150px;
    background: var(--badge); color: var(--badge-text); font-size: 11px;
    padding: 1px 6px; border-radius: 4px;
  }
  .product-name {
    position: absolute; left: 0; width: 100%; top: 176px;
    font-size: 24px; line-height: 30px; font-weight: 400; color: var(--ink); letter-spacing: 0.5px;
  }
  .claims { position: absolute; left: 0; width: 100%; top: 224px; font-size: 13px; line-height: 18.5px; color: #222a16; }

  .arch {
    position: absolute; left: 455px; top: 322px; width: 200px; height: 120px;
    border-radius: 50% 50% 0 0 / 40% 40% 0 0; background: var(--arch);
  }
  .arch-text {
    position: absolute; left: 333px; width: 422px; top: 337px; text-align: center;
    font-size: 10.5px; line-height: 16px; font-weight: 700; color: var(--arch-text);
  }
</style>
</head>
<body>
  <div class="brand-name">Leaf Sentry</div>

  <section class="label">
    <div class="label-face">
      <div class="label-texture" role="img" aria-label="Soft light streaks across the green label background"></div>

      <div class="panel panel-directions">
        <p><span class="lead">Important Note:</span> This product does not replace regular fertilization applications.</p>
        <p>Seeds: (1) Soak seeds in concentrate for 3 hours remove seeds (save &amp; reuse concentrate) rinse, dry and plant. (2) Plant seeds in dirt add 1 teaspoon of concentrate to 16 oz. water and apply to planted seeds.</p>
        <p>Transplant: (1) Add 2 tablespoons to a gallon of water. Pour water into a tray or large container and submerge seedling so that roots are in solution. Leave at least 3 hours and up to 24 hours. (2) After transplanting add ½ teaspoon to the base of plant and water.</p>
        <p>Mature Plant: Add 1 tablespoon to 1 gallon of water and use and use mixture when preparing your favorite fertilizer.</p>
        <div class="spacer"></div>
        <p class="lead">KEEP OUT OF REACH OF CHILDREN</p>
        <p class="lead">WARRANTY</p>
        <p>Verdalis Agrilabs Inc. warrants that this product conforms to the chemical description on the label and is a reasonable fit for the purposes set forth in the Directions on this label when used in accordance with those Directions under the conditions described therein. TO THE EXTENT CONSISTENT WITH APPLICABLE LAW NO OTHER EXPRESS WARRANTY OR IMPLIED WARRANTY OF FITNESS FOR PARTICULAR PURPOSE OR MECHANTABILITY IS MADE. This warranty is also subject to the conditions and limitations stated herein.</p>
      </div>

      <div class="center">
        <p class="company">Verdalis Agrilabs Inc.</p>
        <span class="size-badge">8 oz</span>
        <p class="product-name">Leaf Sentry</p>
        <div class="claims">
          <p>Biocompatible-Biodegradable-Nontoxic</p>
          <p>Safe for Organic Production</p>
          <p>Verdalis Agrilabs Inc. prides itself on developing products that<br>DO NOT harm humans, animals or the planet along with<br>our commitment to sustainability.</p>
        </div>
      </div>

      <div class="arch"></div>
      <div class="arch-text">
        <p>Recommended use</p>
        <p>Active ingredients and Warrant</p>
      </div>

      <div class="panel panel-info">
        <p><span class="lead">Leaf Sentry</span> is a versatile ecologically friendly plant supplement that stimulates the natural innate defense responses within plants to resist insects, pathogens, and soil-borne diseases.</p>
        <p>Leaf Sentry increases photosynthesis, promotes and enhances plant growth, stimulates nutrient uptake, increases germination and sprouting, and boosts plant vigor.</p>
        <p>Our commitment to you is reflected in our full time research center where our scientists are continually researching better ways to improve crop yields along with extensive research on the pre and post-harvest treatment of plants utilizing alternatives to synthetic fungicides, pesticides and fertilizers not only for you but also for the commercial farmer. Leaf Sentry has been specially developed for anyone who loves growing plants.</p>
        <div class="spacer"></div>
        <p class="section-title">Active Ingredient</p>
        <table class="ingredients">
          <tr><td>D-glucosamine- N-acetyl-glucosamine</td><td class="pct">1.00%</td></tr>
          <tr><td>Other Ingredients</td><td class="pct">99.00%</td></tr>
          <tr><td>TOTAL</td><td class="pct">100.00%</td></tr>
        </table>
        <div class="spacer"></div>
        <div class="legal">
          <p>This product is exempt from regulation under 25(b) of FIFRA.</p>
          <p>Manufactured by Verdalis Agrilabs Inc.</p>
          <p>Saguaro Bend, AZ. 85399</p>
          <p>Questions or Comments call (555) 318-4720</p>
        </div>
        <div class="spacer"></div>
        <p class="section-title">Recommended Use</p>
        <p class="body-sm">Leaf Sentry may be applied several ways depending on where your plant is on its life cycle.</p>
      </div>
    </div>
  </section>
</body>
</html>
```